Brochure Design Project

Looking to have a 3 panel (folded) brochure designed for our business.

take inspiration/colorschemes from our upcoming site: www.brightvale.ca/demo

photos and ideas from: www.facebook.com/brightvalecanada
Updates

Lots of new photos uploaded this morning!

New Fonts added to match with our branding. Please use for all main text/headings.

New photo uploaded called 'small'

Please incorporate it into design.

Target Market(s)

Wealthy Home Owners

Industry/Entity Type

Business

Requirements
Must have
• 3 inside panels detail : Home Automation Services (2 of 3 panels) and Home Theater Services (1 of 3 panels).

```html
<!DOCTYPE html>
<html lang="en">
<head>
<meta charset="utf-8">
<title>Brightvale – Tri-fold Brochure</title>
<link rel="stylesheet" href="https://fonts.googleapis.com/css2?family=Source+Sans+3:ital,wght@0,400;0,600;0,700;1,700&display=swap">
<style>
:root{
  --stage:#b47a4c;
  --ink:#0d0d0d;
  --orange:#f39a1e;
  --paper:#ffffff;
  --cream:#f6ead8;
  --text-dark:#222;
  --text-light:#e8e8e8;
  --name:#e2e2e2;
}
*{box-sizing:border-box;margin:0;padding:0}
html,body{width:1200px;height:928px;overflow:hidden}
body{background:var(--stage);font-family:"Source Sans 3",Arial,sans-serif;position:relative}

.sheet-label{position:absolute;color:#fff;font-weight:700;font-size:26px;letter-spacing:.5px;text-align:center}
.sheet-label--front{left:350px;width:523px;top:16px}
.sheet-label--back1{left:57px;width:525px;top:852px}
.sheet-label--back2{left:615px;width:525px;top:852px}

.brochure{position:absolute;display:grid;grid-template-columns:repeat(3,1fr);width:525px;height:370px;box-shadow:0 4px 14px rgba(0,0,0,.45);overflow:hidden}
.brochure--front{left:350px;top:59px;width:523px}
.brochure--back1{left:57px;top:464px}
.brochure--back2{left:615px;top:464px}

.panel{position:relative;overflow:hidden;font-size:6.6px;line-height:1.4}
.panel--dark{background:var(--ink);color:var(--text-light)}
.panel--light{background:var(--paper);color:var(--text-dark)}
.brochure--back1 .panel--light{background:linear-gradient(90deg,#fff 0%,var(--cream) 100%)}
.brochure--back1 .panel--light.panel--mid{background:linear-gradient(90deg,var(--cream) 0%,#fff 40%,#fff 60%,var(--cream) 100%)}

.photo{position:absolute;left:0;width:100%}
.swoop{position:absolute;left:0;width:100%;display:block}

.heading{color:var(--orange);font-weight:700;font-size:10px;display:inline-block;border-bottom:1px solid var(--orange);padding-bottom:1px}
.copy p{margin-bottom:6px}
.copy strong{font-weight:700}

.brand-name{font-weight:600;color:var(--name);line-height:1;white-space:nowrap}

/* front panel 1 */
.about{position:absolute;left:11px;right:9px;top:88px}
.about .heading{margin-bottom:7px;border:0}
.partners{position:absolute;left:11px;right:8px;top:285px;display:grid;grid-template-columns:repeat(3,1fr);gap:6px 5px}
.partners span{height:16px;border:1px solid #555;background:#1a1a1a}
.partners span.wide{background:#2b2b2b}

/* front panel 2 */
.front-name{position:absolute;right:10px;top:274px;font-size:17px}
.contact{position:absolute;right:10px;top:298px;text-align:right;font-size:6.6px}
.contact dt{color:var(--orange);font-weight:700;display:inline}
.contact dd{display:inline;color:#fff}
.contact div{line-height:1.3}
.web{position:absolute;right:10px;bottom:10px;color:#fff;font-size:11px}

/* front panel 3 */
.cover-name{position:absolute;left:18px;top:18px;font-size:22px}
.promo{position:absolute;left:10px;right:8px;top:258px;color:#fff;font-weight:700;font-size:8.4px;line-height:1.35;text-transform:uppercase}
.call{position:absolute;left:10px;top:316px;color:var(--orange);font-weight:700;font-size:14px}
.phone{position:absolute;left:10px;top:334px;color:#fff;font-weight:700;font-style:italic;font-size:19px}

/* back panels */
.brochure--back1 .panel,.brochure--back2 .panel{font-size:7px;line-height:1.45}
.intro{position:absolute;left:9px;right:8px;top:104px}
.intro .heading{margin-bottom:10px}
.services{position:absolute;left:0;right:0;top:10px;text-align:center}
.services .heading{font-size:11px;margin-bottom:8px}
.services__lead{font-size:8.2px;line-height:1.3;padding:0 18px;margin-bottom:20px}
.features{list-style:none;color:var(--orange);font-weight:700;font-size:9px;line-height:1.6;text-transform:uppercase}
.features li::before{content:"\2605\00a0";font-size:6.5px;vertical-align:1px}
.icons{position:absolute;left:4px;right:4px;top:196px;display:grid;grid-template-columns:repeat(3,44px);justify-content:space-between;gap:8px 0;padding:0 4px}
.icons span{height:44px;border:1px solid #777;background:linear-gradient(#ffffff,#d9d9d9)}
.theatre-head{position:absolute;left:0;right:0;top:0;height:80px;background:var(--ink)}
.back-name{position:absolute;left:0;right:0;top:14px;text-align:center;font-size:23px}
.theatre{position:absolute;left:8px;right:8px;top:84px}
.theatre .heading{margin-bottom:6px;border:0;font-size:11px}
.theatre .copy p,.theatre p{margin-bottom:7px}
.theatre__sub{font-weight:700;margin-bottom:8px}
.theatre__list{list-style:none;text-align:center;color:var(--orange);font-weight:700;font-size:9px;line-height:1.4}
.theatre__list span::before{content:"\2605\00a0";font-size:6.5px;vertical-align:1px}
.back-call{position:absolute;left:8px;bottom:10px;color:var(--orange);font-weight:700;font-size:13px;white-space:nowrap}
.back-call em{color:#fff;font-style:italic}
</style>
</head>
<body>

<div class="sheet-label sheet-label--front">Front</div>

<!-- FRONT -->
<section class="brochure brochure--front">
  <div class="panel panel--dark">
    <div class="photo" style="top:0;height:88px;background:linear-gradient(135deg,#1d2733,#07090c 60%,#2b2f38)" role="img" aria-label="Photo of an equipment rack with blue status lights"></div>
    <svg class="swoop" style="top:44px" width="175" height="46" viewBox="0 0 175 46" preserveAspectRatio="none" aria-hidden="true">
      <path d="M0 46 L0 34 Q70 2 175 0 L175 46 Z" fill="#0d0d0d"/>
      <path d="M0 34 Q70 2 175 0" fill="none" stroke="#f39a1e" stroke-width="2"/>
    </svg>
    <div class="about copy">
      <h2 class="heading">About Us</h2>
      <p>You can always rely on Brightvale. Above all else, we pride ourselves on the level of service we provide our clients.</p>
      <p>As technology increasingly becomes part of our lives, it can be confusing, frustrating and sometimes a little overwhelming. At Brightvale, our mission is to bridge the gap between the technology that people want, and the simplicity they need in order to take advantage of it. As our client, you will be provided with friendly, face-to-face service, the highest quality products, and meticulous installation practices. Brightvale has now completed over 1200 unique projects to date. See for yourself – let us be part of your next project. Call Today!</p>
      <p>Brightvale prides itself on partnering with the best companies in the industry. Our main considerations are given to Value, Green-Friendliness, Ease of Use and Innovation.</p>
    </div>
    <div class="partners" aria-label="Partner badges">
      <span></span><span class="wide"></span><span></span>
      <span></span><span class="wide"></span><span></span>
      <span></span><span class="wide"></span><span style="visibility:hidden"></span>
    </div>
  </div>

  <div class="panel panel--dark">
    <div class="photo" style="top:0;height:268px;background:radial-gradient(ellipse at 50% 25%,#f7c36a 0%,#d98a2f 45%,#7a3a18 100%)" role="img" aria-label="Photo of a warmly lit hallway with framed paintings"></div>
    <svg class="swoop" style="top:222px" width="175" height="60" viewBox="0 0 175 60" preserveAspectRatio="none" aria-hidden="true">
      <path d="M0 60 L0 40 Q80 34 175 0 L175 60 Z" fill="#0d0d0d"/>
      <path d="M0 40 Q80 34 175 0" fill="none" stroke="#f39a1e" stroke-width="2"/>
    </svg>
    <div class="brand-name front-name">BRIGHTVALE</div>
    <dl class="contact">
      <div><dt>Office:</dt> <dd>604-555-0142</dd></div>
      <div><dt>Fax:</dt> <dd>604-555-0187</dd></div>
      <div><dt>E-Mail:</dt> <dd>info@brightvale.ca</dd></div>
      <div><dt>Address:</dt> <dd>#210-48 Harbour St.</dd></div>
      <div><dd>Vancouver V6B 0A1</dd></div>
    </dl>
    <div class="web">www.brightvale.ca</div>
  </div>

  <div class="panel panel--dark">
    <div class="brand-name cover-name">BRIGHTVALE</div>
    <div class="photo" style="top:55px;height:200px;background:linear-gradient(180deg,#3c5f9c 0%,#5a6f8d 45%,#b57a3e 75%,#2a1a10 100%)" role="img" aria-label="Photo of a modern house lit up at dusk"></div>
    <svg class="swoop" style="top:50px" width="175" height="30" viewBox="0 0 175 30" preserveAspectRatio="none" aria-hidden="true">
      <path d="M0 0 L175 0 L175 5 Q90 8 0 28 Z" fill="#0d0d0d"/>
      <path d="M175 5 Q90 8 0 28" fill="none" stroke="#f39a1e" stroke-width="1.5"/>
    </svg>
    <svg class="swoop" style="top:222px" width="175" height="36" viewBox="0 0 175 36" preserveAspectRatio="none" aria-hidden="true">
      <path d="M0 36 L0 30 Q90 24 175 0 L175 36 Z" fill="#0d0d0d"/>
      <path d="M0 30 Q90 24 175 0" fill="none" stroke="#ffffff" stroke-width="1.5"/>
    </svg>
    <p class="promo">Brightvale has now completed over 1200 unique projects to date. See for yourself – let us be part of your next project.</p>
    <div class="call">Call Today!</div>
    <div class="phone">604-555-0142</div>
  </div>
</section>

<!-- BACK 1 -->
<section class="brochure brochure--back1">
  <div class="panel panel--light">
    <div class="photo" style="top:0;height:90px;background:linear-gradient(135deg,#1d2733,#07090c 60%,#2b2f38)" role="img" aria-label="Photo of an equipment rack with blue status lights"></div>
    <svg class="swoop" style="top:52px" width="175" height="40" viewBox="0 0 175 40" preserveAspectRatio="none" aria-hidden="true">
      <path d="M0 40 L0 30 Q80 4 175 2 L175 40 Z" fill="#fff"/>
      <path d="M0 30 Q80 4 175 2" fill="none" stroke="#f39a1e" stroke-width="2"/>
    </svg>
    <div class="intro copy">
      <h2 class="heading">Home Automation</h2>
      <p>Home Automation is changing the way we interact with our homes. It is the unification of Media, Climate, Lighting, Security and Access Systems into one easy-to-learn interface</p>
      <p>Home Automation is the future of home systems and home control. It is the amalgamation of all the systems in the home into one easy-to-learn interface. Whether it is a multi-million dollar residence or a small spec house, it is very important to plan and wire for a Home Automation System.</p>
      <p>Brightvale can spec, supply and install a Home Automation System tailored specifically to the project. These systems will immediately add to the value of the home adding convenience and simplicity to its overall operation. These systems are programmed onto Novalink touchscreens, which are completely customizable to cater to the size of home and technical aptitude of the client.</p>
    </div>
  </div>

  <div class="panel panel--light panel--mid">
    <div class="services">
      <h2 class="heading">Home Automation</h2>
      <p class="services__lead">Brightvale's Home Automation System can operate:</p>
      <ul class="features">
        <li>Lighting Systems</li><li>Climate Control</li><li>Security Systems</li>
        <li>CCTV Camera Systems</li><li>Distributed Audio / Video</li><li>Pool Control</li>
      </ul>
    </div>
    <div class="icons">
      <span role="img" aria-label="Speaker icon"></span><span role="img" aria-label="Dial icon"></span><span role="img" aria-label="Light bulb icon"></span>
      <span role="img" aria-label="Disc icon"></span><span role="img" aria-label="Shield icon"></span><span role="img" aria-label="Pool icon"></span>
    </div>
    <div class="photo" style="top:300px;height:70px;background:linear-gradient(180deg,#3a2a1e,#14100c)" role="img" aria-label="Photo of a home theatre room with a large screen"></div>
    <svg class="swoop" style="top:292px" width="175" height="30" viewBox="0 0 175 30" preserveAspectRatio="none" aria-hidden="true">
      <path d="M0 0 L175 0 L175 2 Q90 4 0 26 Z" fill="#fff"/>
      <path d="M175 2 Q90 4 0 26" fill="none" stroke="#f39a1e" stroke-width="2"/>
    </svg>
  </div>

  <div class="panel panel--light">
    <div class="theatre-head"></div>
    <svg class="swoop" style="top:48px" width="175" height="34" viewBox="0 0 175 34" preserveAspectRatio="none" aria-hidden="true">
      <path d="M0 34 L0 26 Q90 4 175 0 L175 34 Z" fill="#fff"/>
      <path d="M0 26 Q90 4 175 0" fill="none" stroke="#f39a1e" stroke-width="2"/>
    </svg>
    <div class="brand-name back-name">BRIGHTVALE</div>
    <div class="theatre copy">
      <h2 class="heading">Home Theatre</h2>
      <p>We design, supply and install Media Rooms and Home Theaters that will amaze you! Whether it is a dedicated space or a multi-purpose area we can bring the Cinema experience home to you.</p>
      <p>Our Home Theater background is where Brightvale has built its name. Servicing Vancouver, Whistler and Kelowna, we offer a 'Complete Solution' approach to your Home Theater or Media Room project.</p>
      <p>Your search for a home theater company that can deliver the best quality performance, visual appeal and ease-of-use has ended. <strong>Your dream Home Theater or Media Room project is just one phone call away!</strong></p>
      <p class="theatre__sub">Our home theater services are:</p>
      <ul class="theatre__list">
        <li><span>Design</span></li>
        <li><span>Installation</span> <span>Calibration</span></li>
        <li><span>Soundproofing</span> <span>Star Ceilings</span></li>
      </ul>
    </div>
    <svg class="swoop" style="top:306px" width="175" height="64" viewBox="0 0 175 64" preserveAspectRatio="none" aria-hidden="true">
      <path d="M0 64 L0 22 Q90 16 175 0 L175 64 Z" fill="#0d0d0d"/>
      <path d="M0 22 Q90 16 175 0" fill="none" stroke="#f39a1e" stroke-width="2.5"/>
    </svg>
    <div class="back-call">Call Today:- <em>604-555-0142</em></div>
  </div>
</section>

<!-- BACK 2 -->
<section class="brochure brochure--back2">
  <div class="panel panel--light">
    <div class="photo" style="top:0;height:90px;background:linear-gradient(135deg,#1d2733,#07090c 60%,#2b2f38)" role="img" aria-label="Photo of an equipment rack with blue status lights"></div>
    <svg class="swoop" style="top:52px" width="175" height="40" viewBox="0 0 175 40" preserveAspectRatio="none" aria-hidden="true">
      <path d="M0 40 L0 30 Q80 4 175 2 L175 40 Z" fill="#fff"/>
      <path d="M0 30 Q80 4 175 2" fill="none" stroke="#f39a1e" stroke-width="2"/>
    </svg>
    <div class="intro copy">
      <h2 class="heading">Home Automation</h2>
      <p>Home Automation is changing the way we interact with our homes. It is the unification of Media, Climate, Lighting, Security and Access Systems into one easy-to-learn interface</p>
      <p>Home Automation is the future of home systems and home control. It is the amalgamation of all the systems in the home into one easy-to-learn interface. Whether it is a multi-million dollar residence or a small spec house, it is very important to plan and wire for a Home Automation System.</p>
      <p>Brightvale can spec, supply and install a Home Automation System tailored specifically to the project. These systems will immediately add to the value of the home adding convenience and simplicity to its overall operation. These systems are programmed onto Novalink touchscreens, which are completely customizable to cater to the size of home and technical aptitude of the client.</p>
    </div>
  </div>

  <div class="panel panel--light panel--mid">
    <div class="services">
      <h2 class="heading">Home Automation</h2>
      <p class="services__lead">Brightvale's Home Automation System can operate:</p>
      <ul class="features">
        <li>Lighting Systems</li><li>Climate Control</li><li>Security Systems</li>
        <li>CCTV Camera Systems</li><li>Distributed Audio / Video</li><li>Pool Control</li>
      </ul>
    </div>
    <div class="icons">
      <span role="img" aria-label="Speaker icon"></span><span role="img" aria-label="Dial icon"></span><span role="img" aria-label="Light bulb icon"></span>
      <span role="img" aria-label="Disc icon"></span><span role="img" aria-label="Shield icon"></span><span role="img" aria-label="Pool icon"></span>
    </div>
    <div class="photo" style="top:300px;height:70px;background:linear-gradient(180deg,#3a2a1e,#14100c)" role="img" aria-label="Photo of a home theatre room with a large screen"></div>
    <svg class="swoop" style="top:292px" width="175" height="30" viewBox="0 0 175 30" preserveAspectRatio="none" aria-hidden="true">
      <path d="M0 0 L175 0 L175 2 Q90 4 0 26 Z" fill="#fff"/>
      <path d="M175 2 Q90 4 0 26" fill="none" stroke="#f39a1e" stroke-width="2"/>
    </svg>
  </div>

  <div class="panel panel--light">
    <div class="theatre-head"></div>
    <svg class="swoop" style="top:48px" width="175" height="34" viewBox="0 0 175 34" preserveAspectRatio="none" aria-hidden="true">
      <path d="M0 34 L0 26 Q90 4 175 0 L175 34 Z" fill="#fff"/>
      <path d="M0 26 Q90 4 175 0" fill="none" stroke="#f39a1e" stroke-width="2"/>
    </svg>
    <div class="brand-name back-name">BRIGHTVALE</div>
    <div class="theatre copy">
      <h2 class="heading">Home Theatre</h2>
      <p>We design, supply and install Media Rooms and Home Theaters that will amaze you! Whether it is a dedicated space or a multi-purpose area we can bring the Cinema experience home to you.</p>
      <p>Our Home Theater background is where Brightvale has built its name. Servicing Vancouver, Whistler and Kelowna, we offer a 'Complete Solution' approach to your Home Theater or Media Room project.</p>
      <p>Your search for a home theater company that can deliver the best quality performance, visual appeal and ease-of-use has ended. <strong>Your dream Home Theater or Media Room project is just one phone call away!</strong></p>
      <p class="theatre__sub">Our home theater services are:</p>
      <ul class="theatre__list">
        <li><span>Design</span></li>
        <li><span>Installation</span> <span>Calibration</span></li>
        <li><span>Soundproofing</span> <span>Star Ceilings</span></li>
      </ul>
    </div>
    <svg class="swoop" style="top:306px" width="175" height="64" viewBox="0 0 175 64" preserveAspectRatio="none" aria-hidden="true">
      <path d="M0 64 L0 22 Q90 16 175 0 L175 64 Z" fill="#0d0d0d"/>
      <path d="M0 22 Q90 16 175 0" fill="none" stroke="#f39a1e" stroke-width="2.5"/>
    </svg>
    <div class="back-call">Call Today:- <em>604-555-0142</em></div>
  </div>
</section>

<div class="sheet-label sheet-label--back1">Back-1</div>
<div class="sheet-label sheet-label--back2">Back-2</div>

</body>
</html>
```